The Lanternwork of Belonging Personal Growth Template

We are creating a two-page Word document titled 'The Lanternwork of Belonging.' This guide/template should embody a professional, clear, and engaging design that facilitates learning and application of DEI principles within a business context.

Target Market(s)

Our primary users are middle to senior management professionals who are responsible for implementing and upholding DEI values within their teams and organizations. The design must resonate with this demographic, implying a sophisticated and functional aesthetic.

Industry/Entity Type

Healthcare, Counseling

Requirements
Must have
• Branding: Incorporate KRB colors for branding consistency. Ensure that the 'Lanternwork of Belonging' is prominently featured within the design. Content Layout: We require a clean, clear, and logical layout that intuitively guides the user through the steps of the DEI Harbor Ladder. Image Redesign: The images pertaining to the assessment and differentiation of self should be recreated to be high-resolution and professionally styled. They should directly support the content and be relatable to our target audience. Accessibility: The template must be easily navigable, with font sizes and styles that ensure readability and ADA compliance. Actionable Steps: Clearly define sections for 'Inspiration,' 'Goal,' and 'Daily Commitment' with examples provided, and allow for user interaction such as note-taking or checkboxes. Reflection Section: Include a 'Two-Week Reflection & Follow-up' section to encourage ongoing engagement with the tool.
Nice to have
• we would appreciate it if the 'Daily Biopsychosocial Commitment Table' could be adjusted to track actions over a four-week period, rather than daily, to align with managerial workflows.
Should not have
• Informal Graphics: Avoid the use of cartoons, silly icons, or figures that could detract from the professional tone of the document. Overcrowding: Prevent a cluttered design by balancing white space with content, ensuring the guide does not overwhelm the user.

```html
<!DOCTYPE html>
<html lang="en">
<head>
<meta charset="utf-8">
<title>The Lanternwork of Belonging – Workplace Wellness Framework</title>
<link rel="stylesheet" href="https://fonts.googleapis.com/css2?family=Manrope:wght@400;500;600;700;800&family=Montserrat:wght@600;700;800;900&display=swap">
<style>
:root{
  --navy:#2b2a64;
  --navy-deep:#1d1c4a;
  --gold:#d39a3a;
  --gold-deep:#b9832c;
  --blue:#6699cc;
  --blue-deep:#4f82b6;
  --panel:#ededf0;
  --lav:#dcdbe6;
  --cream:#f8ecda;
  --cream-soft:#fbf4ea;
  --sky:#e2ebf5;
  --ink:#2a2a3a;
  --page-bg:#d9d9d9;
  --white:#ffffff;
}
*{box-sizing:border-box;margin:0;padding:0}
html,body{width:800px;height:1200px;overflow:hidden}
body{background:var(--page-bg);font-family:"Manrope",sans-serif;color:var(--ink);position:relative}

.sheet{position:absolute;background:var(--white);overflow:hidden}
.sheet--framework{left:65px;top:58px;width:672px;height:519px}
.sheet--table{left:63px;top:604px;width:674px;height:521px}

/* ---------- Framework sheet ---------- */
.masthead{position:absolute;left:0;top:0;width:672px;height:82px}
.masthead svg{position:absolute;left:0;top:0}
.brand{position:absolute;left:18px;top:22px;width:104px;display:flex;flex-direction:column;align-items:center;gap:5px}
.brand__dot{width:34px;height:34px;border-radius:50%;border:2px solid var(--navy)}
.brand__name{font-family:"Manrope",sans-serif;font-weight:700;font-size:7.4px;line-height:1.15;color:var(--navy);text-align:center;letter-spacing:.2px;text-transform:uppercase}
.masthead__title{position:absolute;left:147px;top:28px;width:515px;font-family:"Montserrat",sans-serif;font-weight:700;font-size:9.7px;color:var(--white);white-space:nowrap}
.masthead__title span{color:var(--gold);text-transform:uppercase}
.masthead__purpose{position:absolute;left:147px;top:44px;width:505px;font-size:7.6px;line-height:1.3;color:var(--white)}
.masthead__purpose b{color:var(--gold);font-family:"Montserrat",sans-serif;font-weight:700}

.panel{position:absolute;background:var(--panel);border-radius:12px}
.step-tab{position:absolute;height:28px;background:var(--navy);color:var(--white);display:flex;align-items:center;gap:5px;padding-left:22px;border-radius:10px 4px 18px 4px;clip-path:polygon(6% 0,100% 0,94% 100%,0 100%)}
.step-tab__icon{width:12px;height:12px;border-radius:50%;background:var(--gold);border:2px solid #f3d7a4}
.step-tab__pill{background:var(--white);color:var(--navy);font-family:"Montserrat",sans-serif;font-weight:700;font-size:6.2px;border-radius:6px;padding:1px 5px}
.step-tab__label{font-family:"Montserrat",sans-serif;font-weight:800;font-size:8.2px;letter-spacing:.2px}
.intro{position:absolute;font-size:7px;line-height:1.2;color:var(--ink)}
.subhead{position:absolute;font-size:7.8px;font-weight:700;color:var(--navy);white-space:nowrap}
.subhead small{font-size:3.8px;font-weight:600;display:inline-block;vertical-align:middle;line-height:1.1;margin-left:3px;color:var(--ink)}

.bps{position:absolute;display:grid;border-radius:8px;overflow:hidden;border:1px solid #c9c9d6;background:var(--white)}
.bps__head{font-family:"Manrope",sans-serif;font-weight:700;color:var(--white);text-align:center;display:flex;align-items:center;justify-content:center}
.bps__head--bio{background:var(--navy)}
.bps__head--psycho{background:var(--gold)}
.bps__head--social{background:var(--blue)}
.bps__cell{padding:3px 5px;line-height:1.2;border-top:1px solid #dadae4}
.bps__cell--bio{background:var(--white)}
.bps__cell--bio.alt{background:var(--panel)}
.bps__cell--psycho{background:var(--white);border-left:1px solid #e1d5c3}
.bps__cell--psycho.alt{background:var(--cream-soft)}
.bps__cell--social{background:var(--sky);border-left:1px solid #c8d6e6}
.bps__cell--social.alt{background:var(--white)}
.bullet{position:relative;padding-left:6px;display:block}
.bullet::before{content:"";position:absolute;left:0;top:2px;width:2.6px;height:2.6px;border-radius:50%;border:1px solid var(--navy)}
.bps__cell--psycho .bullet::before{border-color:var(--gold)}
.bps__cell--social .bullet::before{border-color:var(--blue)}
.examples{font-weight:700;display:block;margin-bottom:2px}
.bullet + .bullet{margin-top:6px}

.inspiration .bps{left:14px;top:55px;width:259px;height:127px;grid-template-columns:86px 87px 86px;grid-template-rows:12px 36px 36px 1fr;font-size:5.7px}
.inspiration .bps__head{font-size:8px}

.diff{position:absolute;left:14px;top:48px;width:259px;height:140px}
.diff__card{position:absolute;top:0;height:140px;background:var(--white);border:1px solid #cfcfdb;border-radius:9px;overflow:hidden}
.diff__card--traits{left:0;width:100px}
.diff__card--benefits{left:166px;width:94px}
.diff__cap{height:17px;padding:2px 8px;font-size:5.4px;font-weight:700;line-height:1.05;color:var(--white)}
.diff__card--traits .diff__cap{background:var(--navy);clip-path:polygon(0 0,88% 0,100% 100%,0 100%)}
.diff__card--benefits .diff__cap{background:var(--gold);clip-path:polygon(12% 0,100% 0,100% 100%,0 100%)}
.diff__list{padding:3px 5px 0 7px;font-size:5.7px;line-height:1.13}
.diff__list .bullet + .bullet{margin-top:2.5px}
.diff__card--benefits .bullet::before{border-color:var(--gold)}
.diff__photo{position:absolute;left:96px;top:4px;width:70px;height:136px;border-radius:8px 8px 0 0;background:linear-gradient(160deg,#cfdbe7 0%,#9fb4c9 40%,#5a6f8d 75%,#3f4f6b 100%)}

.commit .bps{left:14px;top:31px;width:572px;height:107px;grid-template-columns:190px 192px 190px;grid-template-rows:17px 31px 1fr;font-size:6px}
.commit .bps__head{font-size:8.4px}

.reflection{position:absolute;left:32px;top:464px;width:520px;height:37px;border:1.4px solid var(--navy);border-radius:9px;overflow:hidden;display:flex}
.reflection__label{width:113px;background:var(--navy);color:var(--white);font-weight:700;font-size:8.8px;line-height:1.2;padding:7px 0 0 15px}
.reflection__notes{flex:1}
.partner{position:absolute;display:flex;align-items:center;gap:4px}
.partner__dot{border-radius:50%;border:2px solid var(--navy);flex:none}
.partner__name{font-family:"Manrope",sans-serif;font-weight:800;color:var(--navy);text-transform:uppercase;line-height:1.05}
.partner--framework{left:563px;top:467px}
.partner--framework .partner__dot{width:26px;height:26px}
.partner--framework .partner__name{font-size:7px}
.sheet__base{position:absolute;left:0;bottom:0;width:100%;height:8px;background:var(--gold)}

/* ---------- Commitment table sheet ---------- */
.tablehead{position:absolute;left:0;top:0;width:100%;height:116px;background:var(--navy)}
.tablehead__title{position:absolute;left:29px;top:22px;font-family:"Montserrat",sans-serif;font-weight:900;font-size:19.6px;color:var(--white);letter-spacing:-.4px;white-space:nowrap}
.tablehead__title span{color:var(--gold)}
.tablehead__brands{position:absolute;left:550px;top:17px;display:flex;gap:8px}
.tablehead__brands .partner{position:static;flex-direction:column;gap:2px;width:46px}
.tablehead__brands .partner__dot{width:15px;height:15px;border-color:var(--white)}
.tablehead__brands .partner__name{font-size:4.4px;color:var(--white);text-align:center}

.tracker{position:absolute;left:29px;top:51px;width:616px;display:grid;grid-template-columns:16px 271px 47px 44px 50px 47px 47px 47px 47px;grid-template-rows:29px 19px 39px 39px 39px 19px 39px 39px 39px 19px 40px 40px 40px;border-radius:8px;overflow:hidden;background:var(--white);border:1px solid #cfd2dd}
.tracker__action{grid-column:1 / span 2;background:var(--gold);color:var(--white);font-family:"Montserrat",sans-serif;font-weight:800;font-size:8.8px;display:flex;align-items:center;padding-left:19px;letter-spacing:-.1px;white-space:nowrap}
.tracker__day{font-family:"Montserrat",sans-serif;font-weight:800;font-size:6.6px;display:flex;align-items:center;justify-content:center;text-transform:uppercase;letter-spacing:-.1px;white-space:nowrap}
.tracker__day--plain{background:var(--white);color:var(--ink)}
.tracker__day--gold{background:var(--gold);color:var(--white)}
.tracker__day--blue{background:var(--blue);color:var(--white)}
.tracker__section{grid-column:1 / -1;font-family:"Montserrat",sans-serif;font-weight:800;font-size:9.8px;color:var(--white);display:flex;align-items:center;padding-left:24px}
.tracker__section--bio{background:var(--navy)}
.tracker__section--psycho{background:var(--gold)}
.tracker__section--social{background:var(--blue)}
.tracker__num{color:var(--white);font-weight:700;font-size:7.4px;display:flex;align-items:center;justify-content:center}
.bio .tracker__num{background:var(--navy)}
.bio .tracker__num.alt{background:var(--navy-deep)}
.psycho .tracker__num{background:var(--gold)}
.psycho .tracker__num.alt{background:var(--gold-deep)}
.social .tracker__num{background:var(--blue)}
.social .tracker__num.alt{background:var(--blue-deep)}
.tracker__task{display:flex;align-items:center;padding:0 12px 0 7px;font-size:8.8px;font-weight:500;line-height:1.15;color:var(--ink);border-bottom:1px solid #9ea2b3;border-right:1px solid #9ea2b3}
.tracker__cell{border-right:1px solid #c7c9d3;border-bottom:1px solid #9ea2b3}
.tracker__cell:nth-child(9n){border-right:none}
.wk-lav{background:linear-gradient(to bottom,var(--lav) 0 25%,var(--white) 25% 50%,var(--lav) 50% 75%,var(--white) 75% 100%)}
.wk-cream{background:linear-gradient(to bottom,var(--cream) 0 25%,var(--white) 25% 50%,var(--cream) 50% 75%,var(--white) 75% 100%)}
.wk-sky{background:linear-gradient(to bottom,var(--sky) 0 25%,var(--white) 25% 50%,var(--sky) 50% 75%,var(--white) 75% 100%)}
.bio,.psycho,.social{display:contents}
</style>
</head>
<body>

<!-- ================= Framework sheet ================= -->
<section class="sheet sheet--framework">
  <header class="masthead">
    <svg width="672" height="82" viewBox="0 0 672 82">
      <polygon points="111,0 672,0 672,78 138,78" fill="#2b2a64"/>
      <polygon points="138,78 672,78 672,82 139,82" fill="#d39a3a"/>
    </svg>
    <div class="brand">
      <div class="brand__dot"></div>
      <div class="brand__name">The Lanternwork<br>of Belonging</div>
    </div>
    <h1 class="masthead__title"><span>Workplace Wellness for Challenging Times:</span> A Biopsychosocial &amp; Differentiation Framework</h1>
    <p class="masthead__purpose"><b>PURPOSE:</b> This template is designed to help individuals integrate DEI principles into their professional lives by identifying and committing to personal growth areas aligned with Systems and Bowen Theory.</p>
  </header>

  <!-- Step 1 -->
  <div class="panel inspiration" style="left:32px;top:103px;width:286px;height:194px">
    <p class="intro" style="left:14px;top:16px;width:250px">Choose an attribute from the bio-psycho-social assessment to improve wellness and effectiveness.</p>
    <p class="subhead" style="left:13px;top:39px">Leaders Renew Spirit, Build Resilience and Foster Well-Being</p>
    <div class="bps">
      <div class="bps__head bps__head--bio">Bio</div>
      <div class="bps__head bps__head--psycho">Psycho</div>
      <div class="bps__head bps__head--social">Social</div>
      <div class="bps__cell bps__cell--bio alt"><span class="bullet">I am aware of how family, culture, and experiences affect how I think and behave.</span></div>
      <div class="bps__cell bps__cell--psycho alt"><span class="bullet">I foster a psychologically safe environment to acknowledge, discuss and address emotional and polarizing issues.</span></div>
      <div class="bps__cell bps__cell--social"><span class="bullet">I consistently find ways to show appreciation during stressful and uncertain situations.</span></div>
      <div class="bps__cell bps__cell--bio"><span class="bullet">I am aware of neurodiversity and how to leverage it for success</span></div>
      <div class="bps__cell bps__cell--psycho"><span class="bullet">I instill the confidence that views and perspectives will be acknowledged and considered.</span></div>
      <div class="bps__cell bps__cell--social alt"><span class="bullet">I cultivate a broad and culturally diverse network of individuals to exchange ideas and make decisions.</span></div>
      <div class="bps__cell bps__cell--bio alt"><span class="bullet">I nurture body and spirit in a manner that fosters hope, empathy, and grace.</span></div>
      <div class="bps__cell bps__cell--psycho alt"><span class="bullet">I am aware of unique talent(s), or strength(s) and how to nurture them.</span></div>
      <div class="bps__cell bps__cell--social"><span class="bullet">I use my power in visible and subtle ways to include people and discourage exclusion.</span></div>
    </div>
  </div>
  <div class="step-tab" style="left:22px;top:90px;width:150px">
    <span class="step-tab__icon"></span><span class="step-tab__pill">STEP 1</span><span class="step-tab__label">INSPIRATION</span>
  </div>

  <!-- Step 2 -->
  <div class="panel goal" style="left:351px;top:103px;width:286px;height:194px">
    <p class="intro" style="left:14px;top:15px;width:240px">Choose an attribute from differentiation of self to improve wellness and uniqueness.</p>
    <p class="subhead" style="left:13px;top:35px">Differentiation of Self (Fostering Uniqueness)<small>How do we foster "Differentiation of Self"<br>for themselves and others"</small></p>
    <div class="diff">
      <div class="diff__card diff__card--traits">
        <div class="diff__cap">"Differentiation of Self"<br>Charactenstics</div>
        <div class="diff__list">
          <span class="bullet">Be an interdependent member of the group.</span>
          <span class="bullet">Maintain beliefs and attitudes in the face of pressure to conform.</span>
          <span class="bullet">Resotve problems rather than let them fester</span>
          <span class="bullet">Self-validate</span>
          <span class="bullet">Self-soothe</span>
          <span class="bullet">Tolerate short-term discomfort. or gratification for long-term growth</span>
          <span class="bullet">Talking action</span>
        </div>
      </div>
      <div class="diff__photo" role="img" aria-label="Photo of colleagues reviewing a tablet together in a bright office"></div>
      <div class="diff__card diff__card--benefits">
        <div class="diff__cap">&nbsp;&nbsp;&nbsp;"Differentiation of Self"<br>&nbsp;&nbsp;&nbsp;benefits</div>
        <div class="diff__list">
          <span class="bullet">A sense of congruence within yourself « pride and confidence in yourself</span>
          <span class="bullet">Highly self-aware - greater capacity to be aware of others Highly differentiated - better at handing stress/anxiety Positive feelings can become saif-perpetuating.</span>
          <span class="bullet">Increased differentiation by one member wil Ukely lead other members to become more Gfferentiated. Ownership of self</span>
        </div>
      </div>
    </div>
  </div>
  <div class="step-tab" style="left:341px;top:90px;width:150px">
    <span class="step-tab__icon"></span><span class="step-tab__pill">STEP 2</span><span class="step-tab__label">GOAL</span>
  </div>

  <!-- Step 3 -->
  <div class="panel commit" style="left:32px;top:318px;width:604px;height:138px">
    <p class="intro" style="left:0;top:18px;width:604px;text-align:center">Define specific, daily actions to help you work towards your well-being and differentiation goals, ultimately enhancing DEI implementation in your job.</p>
    <div class="bps">
      <div class="bps__head bps__head--bio">Bio</div>
      <div class="bps__head bps__head--psycho">Psycho</div>
      <div class="bps__head bps__head--social">Social</div>
      <div class="bps__cell bps__cell--bio" style="padding:5px 9px"><span class="bullet">In the 'Bio' category, actions could include self-care practices that enable one to be an effective DEI advocate even under stress.</span></div>
      <div class="bps__cell bps__cell--psycho" style="padding:5px 14px"><span class="bullet">'Psycho' actions may involve education and reflection on one's cultural competencies and biases.</span></div>
      <div class="bps__cell bps__cell--social alt" style="padding:5px 9px"><span class="bullet">'Social' commitments could be activities that promote inclusion and equity within one's immediate professional sphere.</span></div>
      <div class="bps__cell bps__cell--bio alt" style="padding:5px 9px"><span class="examples">Examples include</span><span class="bullet">Practice mindfulness to maintain resilience when discussing DEI topics in polarized settings.</span><span class="bullet">Engage in physical activities that improve mental clarity to approach DEI work with a non-anxious presence.</span></div>
      <div class="bps__cell bps__cell--psycho alt" style="padding:5px 14px"><span class="examples">Examples include</span><span class="bullet">Reflect daily on personal biases to foster a mindset open to DEI learning and transformation.</span><span class="bullet">Write a journal about DEI progress to reinforce learning and personal growth in DEI competencies.</span></div>
      <div class="bps__cell bps__cell--social" style="padding:5px 9px"><span class="examples">Examples include</span><span class="bullet">Initiate conversations about DEI with colleagues to understand diverse perspectives.</span><span class="bullet">Lead by example in inclusive behaviors, ensuring all team members feel valued and heard.</span></div>
    </div>
  </div>
  <svg style="position:absolute;left:226px;top:306px" width="220" height="26" viewBox="0 0 220 26">
    <path d="M0 8 Q4 0 14 0 H206 Q216 0 220 8 L206 8 Q196 26 180 26 H40 Q24 26 14 8 Z" fill="#2b2a64"/>
  </svg>
  <div style="position:absolute;left:268px;top:311px;display:flex;align-items:center;gap:5px;color:#fff">
    <span class="step-tab__icon"></span><span class="step-tab__pill">STEP 3</span><span class="step-tab__label">DAILY COMMITMENT</span>
  </div>

  <div class="reflection">
    <div class="reflection__label">Two-Week<br>Reflection &amp; Follow</div>
    <div class="reflection__notes"></div>
  </div>
  <div class="partner partner--framework">
    <span class="partner__dot"></span><span class="partner__name">The Kestrel<br>Rowe Group</span>
  </div>
  <div class="sheet__base"></div>
</section>

<!-- ================= Commitment table sheet ================= -->
<section class="sheet sheet--table">
  <div class="tablehead">
    <h2 class="tablehead__title">DAILY BIOPSYCHOSOCIAL <span>COMMITMENT TABLE</span></h2>
    <div class="tablehead__brands">
      <div class="partner"><span class="partner__dot"></span><span class="partner__name">The Lanternwork<br>of Belonging</span></div>
      <div class="partner"><span class="partner__dot"></span><span class="partner__name">The Kestrel<br>Rowe Group</span></div>
    </div>
  </div>

  <div class="tracker">
    <div class="tracker__action">ACTION / THE DAY ACTION WAS TAKEN OVER 4 WEEKS</div>
    <div class="tracker__day tracker__day--plain">Monday</div>
    <div class="tracker__day tracker__day--gold">Tuesday</div>
    <div class="tracker__day tracker__day--blue">Wednesday</div>
    <div class="tracker__day tracker__day--plain">Thursday</div>
    <div class="tracker__day tracker__day--gold">Friday</div>
    <div class="tracker__day tracker__day--blue">Saturday</div>
    <div class="tracker__day tracker__day--plain">Sunday</div>

    <div class="bio">
      <div class="tracker__section tracker__section--bio">BIO</div>
      <div class="tracker__num">1</div><div class="tracker__task">Engage in 16-8 intermitted fasting to address GERD</div>
      <div class="tracker__cell wk-lav"></div><div class="tracker__cell wk-lav"></div><div class="tracker__cell wk-lav"></div><div class="tracker__cell wk-lav"></div><div class="tracker__cell wk-lav"></div><div class="tracker__cell wk-lav"></div><div class="tracker__cell wk-lav"></div>
      <div class="tracker__num alt">2</div><div class="tracker__task">Complete 28-day body-weight strength training</div>
      <div class="tracker__cell wk-cream"></div><div class="tracker__cell wk-cream"></div><div class="tracker__cell wk-cream"></div><div class="tracker__cell wk-cream"></div><div class="tracker__cell wk-cream"></div><div class="tracker__cell wk-cream"></div><div class="tracker__cell wk-cream"></div>
      <div class="tracker__num">3</div><div class="tracker__task">Incorporate daily Natto into daily diet</div>
      <div class="tracker__cell wk-sky"></div><div class="tracker__cell wk-sky"></div><div class="tracker__cell wk-sky"></div><div class="tracker__cell wk-sky"></div><div class="tracker__cell wk-sky"></div><div class="tracker__cell wk-sky"></div><div class="tracker__cell wk-sky"></div>
    </div>

    <div class="psycho">
      <div class="tracker__section tracker__section--psycho">PSYCHO</div>
      <div class="tracker__num">1</div><div class="tracker__task">Complete night Neurofeedback digital sleeping pill to improve sleep and understand Neurofeedback coaching</div>
      <div class="tracker__cell wk-lav"></div><div class="tracker__cell wk-lav"></div><div class="tracker__cell wk-lav"></div><div class="tracker__cell wk-lav"></div><div class="tracker__cell wk-lav"></div><div class="tracker__cell wk-lav"></div><div class="tracker__cell wk-lav"></div>
      <div class="tracker__num alt">2</div><div class="tracker__task">Incorporate Insight Dialogue into client sessions</div>
      <div class="tracker__cell wk-cream"></div><div class="tracker__cell wk-cream"></div><div class="tracker__cell wk-cream"></div><div class="tracker__cell wk-cream"></div><div class="tracker__cell wk-cream"></div><div class="tracker__cell wk-cream"></div><div class="tracker__cell wk-cream"></div>
      <div class="tracker__num">3</div><div class="tracker__task">Complete daily morning box-breathing</div>
      <div class="tracker__cell wk-sky"></div><div class="tracker__cell wk-sky"></div><div class="tracker__cell wk-sky"></div><div class="tracker__cell wk-sky"></div><div class="tracker__cell wk-sky"></div><div class="tracker__cell wk-sky"></div><div class="tracker__cell wk-sky"></div>
    </div>

    <div class="social">
      <div class="tracker__section tracker__section--social">BIO</div>
      <div class="tracker__num">1</div><div class="tracker__task">Join and participate in the Vancouver Jazz Meet-Up</div>
      <div class="tracker__cell wk-lav"></div><div class="tracker__cell wk-lav"></div><div class="tracker__cell wk-lav"></div><div class="tracker__cell wk-lav"></div><div class="tracker__cell wk-lav"></div><div class="tracker__cell wk-lav"></div><div class="tracker__cell wk-lav"></div>
      <div class="tracker__num alt">2</div><div class="tracker__task">Plan 2-annual guys trip with Marcus</div>
      <div class="tracker__cell wk-cream"></div><div class="tracker__cell wk-cream"></div><div class="tracker__cell wk-cream"></div><div class="tracker__cell wk-cream"></div><div class="tracker__cell wk-cream"></div><div class="tracker__cell wk-cream"></div><div class="tracker__cell wk-cream"></div>
      <div class="tracker__num">3</div><div class="tracker__task" style="border-bottom:none">Plan the annual couples’ trip with Marcus &amp; Elena</div>
      <div class="tracker__cell wk-sky" style="border-bottom:none"></div><div class="tracker__cell wk-sky" style="border-bottom:none"></div><div class="tracker__cell wk-sky" style="border-bottom:none"></div><div class="tracker__cell wk-sky" style="border-bottom:none"></div><div class="tracker__cell wk-sky" style="border-bottom:none"></div><div class="tracker__cell wk-sky" style="border-bottom:none"></div><div class="tracker__cell wk-sky" style="border-bottom:none"></div>
    </div>
  </div>
  <div class="sheet__base" style="height:10px"></div>
</section>

</body>
</html>
```